MOREVI VEGAN SUSHI

www.morevi-restaurant.de
We are open in 2018 and are an innovative restaurant from Munich. We would like a cool design for our drinks and food menu. It's very simple at the moment. See the File menu. In any case, our logo should appear. On the website we use neutraface as a font. But it's not a must. We are only open in the evening and appeal to a young, upscale audience.

```html
<!DOCTYPE html>
<html lang="de">
<head>
<meta charset="utf-8">
<title>MOREVI – Menü</title>
<link href="https://fonts.googleapis.com/css2?family=Nunito+Sans:ital,wght@0,300;0,400;0,600;1,300;1,400&display=swap" rel="stylesheet">
<style>
  :root {
    --ink: #111111;
    --accent: #0b7aa1;
    --sky: #d7e8f0;
    --deep-blue: #0b6f99;
    --peach: #f6a072;
    --sand: #f2dccb;
    --paper: #ffffff;
  }
  html, body { margin: 0; padding: 0; overflow: hidden; background: var(--paper); }
  .menu {
    position: relative; width: 848px; height: 1200px; overflow: hidden;
    background: var(--paper); color: var(--ink);
    font-family: "Nunito Sans", "Helvetica Neue", sans-serif; font-weight: 400;
  }
  .decor { position: absolute; left: 0; top: 0; width: 848px; height: 1200px; }
  .brand { position: absolute; left: 70px; top: 62px; width: 190px; text-align: center; }
  .brand-dot { width: 96px; height: 96px; border-radius: 50%; background: var(--ink); margin: 0 auto 58px; }
  .brand-name { font-size: 22px; font-weight: 300; letter-spacing: 13px; margin-right: -13px; line-height: 1; }
  .offer { position: absolute; text-align: center; font-size: 16.4px; line-height: 22px; }
  .offer h2 { margin: 0; color: var(--accent); font-weight: 400; font-size: 24.5px; line-height: 28px; }
  .offer p { margin: 0; }
  .offer em { font-style: italic; }
  .offer .price { font-size: 23px; line-height: 30px; font-weight: 600; margin-top: 4px; }
  .chef { left: 0; width: 848px; top: 282px; }
  .chef p { line-height: 23px; }
  .omakase { left: 0; width: 848px; top: 455px; }
  .omakase p { line-height: 20.5px; }
  .set { top: 628px; width: 280px; }
  .set p { line-height: 22.8px; }
  .set-1 { left: 8px; }
  .set-2 { left: 277px; top: 630px; }
  .set-3 { left: 548px; }
</style>
</head>
<body>
<main class="menu">
  <svg class="decor" viewBox="0 0 848 1200" aria-hidden="true">
    <polygon points="362,0 848,0 848,30 616,125 479,130" fill="var(--sky)"/>
    <polygon points="0,944 185,1023 0,1094" fill="var(--sand)"/>
    <polygon points="0,1094 185,1023 609,1200 0,1200" fill="var(--peach)"/>
    <polygon points="534,1200 848,1036 848,1200" fill="var(--deep-blue)"/>
  </svg>

  <div class="brand">
    <div class="brand-dot"></div>
    <div class="brand-name">MOREVI</div>
  </div>

  <section class="offer chef">
    <h2>CHEF MENÜ mit Aperitiv</h2>
    <p><em>für 2 Personen</em></p>
    <p>Kleine Portion RAMENSUPPE <em>mit Gemüse &amp; Nudeln</em></p>
    <p>MINI SET</p>
    <p>DESSERT</p>
    <p class="price">81,00€</p>
  </section>

  <section class="offer omakase">
    <h2>OMAKASE</h2>
    <p><em>für 2 Personen</em></p>
    <p>EDAMAME</p>
    <p>OMAKASE SET <em>mit 8 Spezialitäten des Hauses</em></p>
    <p>PANA COTTA <em>mit Beeren</em></p>
    <p class="price">68,00€</p>
  </section>

  <section class="offer set set-1">
    <h2>SET 1</h2>
    <p>HOSOMAKI</p>
    <p>FUTOMAKI</p>
    <p>NIGIRI</p>
    <p>KÜRBISKROKETTEN</p>
    <p>WAKAME GURKEN SALAT</p>
    <p>PICKLES</p>
    <p>GYOZA TEIGTASCHEN</p>
    <p>SUSHI CAKE</p>
    <p class="price">33,90€</p>
  </section>

  <section class="offer set set-2">
    <h2>SET 2</h2>
    <p>HOSOMAKI</p>
    <p>FUTOMAKI</p>
    <p>PICKLES</p>
    <p>SUSHI “THUNA” CAKE</p>
    <p>Crispy AUBERGINEN <em>mit Mayo</em></p>
    <p>AUBERGINE DENGAKU</p>
    <p class="price">31,90€</p>
  </section>

  <section class="offer set set-3">
    <h2>SET 3</h2>
    <p>HOSOMAKI</p>
    <p>URAMAKI</p>
    <p>NIGIRI</p>
    <p>GEMÜSE TEMPURA</p>
    <p>Crispy TOFUSTICKS <em>mit Mayo</em></p>
    <p>WAKAME SHIRA AE</p>
    <p class="price">28,90€</p>
  </section>
</main>
</body>
</html>
```